modernized upgrade to existing squarespace site

Hello! I have the following page for my consulting firm: https://fernwaystrategygroup.com/ Would love to upgrade to something more modern/attractive like here: https://www.lobrettiandco.com/ or https://quillbrightlab.com/ , but I am open to creativity. Would like to retain the logo look and color theme from the logo. The rest can be left to creative discretion.

```html
<!DOCTYPE html>
<html lang="en">
<head>
<meta charset="utf-8">
<title>Fernway Strategy Group</title>
<link href="https://fonts.googleapis.com/css2?family=Poppins:wght@400;500&family=Tinos:wght@400;700&display=swap" rel="stylesheet">
<style>
:root{
  --rose:#c6928a;
  --rose-dark:#b57d74;
  --ink:#1d1d1d;
  --body:#3a3a3a;
  --grey-bg:#efefef;
  --card:#ffffff;
  --navy:#1f3550;
  --black:#0c0c0c;
  --star:#f0a01e;
}
*{margin:0;padding:0;box-sizing:border-box}
html,body{width:1200px;height:4005px;overflow:hidden}
body{position:relative;background:#fff;font-family:"Poppins",sans-serif;color:var(--body)}
.abs{position:absolute}
.btn{position:absolute;display:flex;align-items:center;justify-content:center;background:var(--rose);color:#fff;font-size:12px}
.eyebrow{color:var(--rose);font-size:14px;letter-spacing:.5px}
.rule{position:absolute;height:2px;background:var(--rose)}

/* header */
.header{top:0;left:0;width:1200px;height:78px;background:#fff}
.brand{display:flex;align-items:center;gap:10px}
.brand-mark{width:54px;height:54px;border:2px solid var(--rose)}
.brand-name{font-family:"Tinos",serif;font-size:22px;line-height:1.05;color:var(--ink);letter-spacing:1px}
.brand-name small{display:block;font-size:12px;color:var(--rose);letter-spacing:1.5px}
.nav{top:30px;left:450px;display:flex;gap:36px;font-size:13px;color:var(--ink)}
.nav .active{color:var(--rose)}
.nav-social{width:14px;height:14px;border-radius:50%;border:1.5px solid var(--rose);margin-top:2px}
.header-cta{top:0;left:970px;width:230px;height:78px;font-size:18px}

/* hero */
.hero{top:78px;left:0;width:1200px;height:528px;background:linear-gradient(90deg,#eef0f1 0%,#e6e9ea 45%,#c9ced3 70%,#9fa8b1 100%)}
.hero-title{top:200px;left:140px;font-family:"Tinos",serif;font-weight:400;font-size:44px;line-height:58px;color:var(--ink)}
.hero-title b{font-weight:700}

/* about */
.about-photo-a{top:692px;left:141px;width:319px;height:396px;background:linear-gradient(135deg,#eaf1f6,#b9cfe0 60%,#dfe6ec)}
.about-frame{top:752px;left:176px;width:300px;height:355px;border:2px solid var(--rose)}
.about-photo-b{top:897px;left:382px;width:198px;height:234px;background:linear-gradient(180deg,#e4e0da,#9aa0a8 60%,#5c6a7c)}
.about-copy{top:690px;left:643px;width:420px}
.about-copy h2{font-family:"Tinos",serif;font-weight:400;font-size:30px;color:var(--ink);margin-top:4px;white-space:nowrap}
.about-copy p{font-size:12px;line-height:21.7px;letter-spacing:.45px;margin-top:10px}
.about-copy .btn{position:static;width:128px;height:41px;margin-top:24px}

/* services */
.services{top:1217px;left:0;width:1200px;height:595px;background:var(--grey-bg)}
.center{width:1200px;text-align:center}
.section-title{font-family:"Tinos",serif;font-size:31px;color:var(--ink)}
.svc-card{position:absolute;top:1394px;width:289px;height:261px;background:var(--card);text-align:center;padding:28px 30px 0}
.svc-card svg{display:block;margin:0 auto}
.svc-card h3{font-family:"Tinos",serif;font-size:16px;color:var(--ink);margin:14px 0 6px}
.svc-card p{font-size:12.5px;line-height:21.7px}

/* media */
.media-box{position:absolute;top:1897px;width:168px;height:105px;background:#fff;box-shadow:0 3px 10px rgba(0,0,0,.08);display:flex;align-items:center;justify-content:center;font-size:18px;font-weight:500;color:var(--ink);white-space:nowrap}
.round-arrow{position:absolute;width:34px;height:34px;border-radius:50%;display:flex;align-items:center;justify-content:center}

/* feature */
.feature-photo{position:absolute;top:2090px;width:442px;height:429px}
.feature-caption{position:absolute;top:2449px;width:368px;height:126px;background:#fff;box-shadow:0 6px 18px rgba(0,0,0,.1);text-align:center;padding-top:24px}
.feature-caption p{font-family:"Tinos",serif;font-size:17px;line-height:25px;color:var(--ink)}
.feature-caption span{display:inline-block;margin-top:10px;font-size:12px;color:var(--rose);text-decoration:underline}

/* testimonials */
.testimonials{top:2685px;left:0;width:1200px;height:592px;background:linear-gradient(180deg,#2e4a68 0%,#304a66 55%,#1f3550 70%,#24405f 100%)}
.t-card{position:absolute;top:2862px;width:289px;height:331px;background:linear-gradient(180deg,#fff,#f1f1f1);text-align:center;padding-top:31px}
.avatar{width:66px;height:66px;margin:0 auto;border:2px solid #ddd;background:linear-gradient(180deg,#b8c7b0,#6f8468)}
.t-card h4{font-family:"Tinos",serif;font-size:16px;color:var(--ink);margin:24px 0 6px}
.t-card p{font-size:12.5px;line-height:21.7px;padding:0 25px}
.stars{color:var(--star);font-size:18px;letter-spacing:4px;margin-top:14px}

/* cta */
.cta{top:3363px;left:141px;width:917px;height:233px;background:var(--rose);text-align:center;padding-top:48px}
.cta p{font-family:"Tinos",serif;font-size:28px;line-height:41px;color:#fbeeea}
.cta .btn{position:static;margin:16px auto 0;width:127px;height:42px;background:var(--black)}

/* footer */
.footer{top:3681px;left:0;width:1200px;height:324px;background:var(--black);color:#fff}
.footer h5{font-family:"Tinos",serif;font-size:16px;font-weight:400}
.footer h5::after{content:"";display:block;width:24px;height:2px;background:#fff;margin-top:6px}
.footer ul{list-style:none;font-size:12.5px;line-height:23.5px;margin-top:10px}
.f-line{display:flex;gap:10px;font-size:12.5px;line-height:17px;margin-top:14px}
.footer-rule{top:282px;left:141px;width:917px;height:1px;background:#333}
.copy{top:294px;left:0;width:1200px;text-align:center;font-size:12px}
</style>
</head>
<body>

<header class="abs header">
  <div class="abs brand" style="top:11px;left:141px">
    <div class="brand-mark"></div>
    <div class="brand-name">FERNWAY<small>STRATEGY GROUP</small></div>
  </div>
  <nav class="abs nav">
    <span class="active">Home</span><span>Services</span><span>Research</span><span>The Institute</span><span>In The News</span><span class="nav-social"></span>
  </nav>
  <div class="btn header-cta">Contact Us</div>
</header>

<section class="abs hero" role="img" aria-label="Photo of a team of smiling consultants gathered around a laptop in a bright office"></section>
<h1 class="abs hero-title">Macro Economic<br>&amp; Policy Analytics<br>For Today’s <b>Turbulent</b><br><b>Environment</b></h1>

<div class="abs about-frame"></div>
<div class="abs about-photo-a" role="img" aria-label="Photo of a hand using a laptop showing charts and dashboards"></div>
<div class="abs about-photo-b" role="img" aria-label="Photo of three professionals talking in an office corridor"></div>
<div class="abs about-copy">
  <div class="eyebrow">ABOUT</div>
  <h2>FERNWAY STRATEGY GROUP</h2>
  <div style="width:85px;height:2px;background:var(--rose);margin-top:8px"></div>
  <p style="margin-top:18px">Our services suite focuses on providing exclusive, custom research and analytics to a select number of clients. We do so by outlining a sophisticated research plan, building teams of industry experts, and providing final analyses catered to your preferred audience. There is no one-size approach to economic policy research, as such we maintain an ongoing exchange of findings and viewpoints, involving your deep industry knowledge and direction throughout the life of a proposed project.</p>
  <p>Knowing that messaging must cater to final, intended audiences, our reports are written in a manner accessible to your end-user, developed by our in-house communications experts.</p>
  <div class="btn">Read More</div>
</div>

<section class="abs services"></section>
<div class="abs center eyebrow" style="top:1298px">WHAT WE DO</div>
<div class="abs center section-title" style="top:1316px">OUR SERVICES</div>
<div class="rule" style="top:1361px;left:558px;width:84px"></div>

<div class="svc-card" style="left:141px">
  <svg width="58" height="58" viewBox="0 0 58 58" fill="none" stroke="#222" stroke-width="2"><rect x="3" y="5" width="52" height="46" rx="2"/><line x1="3" y1="14" x2="55" y2="14"/><rect x="10" y="34" width="6" height="12"/><rect x="22" y="28" width="6" height="18"/><rect x="34" y="22" width="6" height="24"/><polyline points="10,28 22,22 34,16 48,22" stroke="#c6928a"/></svg>
  <h3>Analytics &amp; Messaging</h3>
  <p>Our communications team can develop influential messaging, in conjunction with our data scientists' technical expertise.</p>
</div>
<div class="svc-card" style="left:455px">
  <svg width="58" height="58" viewBox="0 0 58 58" fill="none" stroke="#222" stroke-width="2"><path d="M14 3h26l10 10v42H14z"/><path d="M40 3v10h10"/><circle cx="14" cy="20" r="9"/><path d="M14 11v9h9" stroke="#c6928a"/><polyline points="22,46 30,36 36,41 44,30" stroke="#c6928a"/></svg>
  <h3>Customized Reports</h3>
  <p>From succinct summations of economic and policy impact to full-length analyses, we can create the customized exposition that best represents your interests.</p>
</div>
<div class="svc-card" style="left:769px">
  <svg width="58" height="58" viewBox="0 0 58 58" fill="none" stroke="#222" stroke-width="2"><circle cx="20" cy="18" r="9"/><path d="M4 52c0-12 7-20 16-20s16 8 16 20z"/><path d="M36 16l9-8 9 8v10H36z" stroke="#c6928a"/><rect x="25" y="38" width="14" height="12"/></svg>
  <h3>Proprietary Surveys</h3>
  <p>Exclusive, custom-designed surveys can enrich your databank, while maintaining access to proprietary resources, establishing you and your firm as a thought leader.</p>
</div>
<div class="btn" style="top:1684px;left:536px;width:127px;height:42px">Contact Us</div>

<div class="round-arrow" style="top:1932px;left:93px;background:#ddd"><svg width="14" height="14" viewBox="0 0 14 14"><path d="M12 7H2M6 3L2 7l4 4" stroke="#555" stroke-width="2" fill="none"/></svg></div>
<div class="media-box" style="left:141px">Ledgerline</div>
<div class="media-box" style="left:329px">Brightwave News</div>
<div class="media-box" style="left:516px">Tickerpoint</div>
<div class="media-box" style="left:702px">Marketloop</div>
<div class="media-box" style="left:889px">Civic Radio</div>
<div class="round-arrow" style="top:1932px;left:1071px;background:var(--rose)"><svg width="14" height="14" viewBox="0 0 14 14"><path d="M2 7h10M8 3l4 4-4 4" stroke="#fff" stroke-width="2" fill="none"/></svg></div>

<div class="feature-photo" style="left:141px;background:linear-gradient(160deg,#f3f4f5,#dfe6ec 50%,#9fb3c6)" role="img" aria-label="Photo of a notebook, pen and tablet on a printed line chart"></div>
<div class="feature-photo" style="left:629px;background:linear-gradient(150deg,#c5d4e4,#e8eef4 45%,#8fa5bd)" role="img" aria-label="Photo of stacked folded newspapers showing business sections"></div>
<div class="feature-caption" style="left:177px"><p>Sophisticated research &amp; a typical analyses<br>for improved communications.</p><span>Learn More</span></div>
<div class="feature-caption" style="left:665px"><p>Proprietary public relations tools<br>that guarantee media visibility.</p><span>Learn More</span></div>

<section class="abs testimonials" role="img" aria-label="Photo of a city skyline across a river at dusk"></section>
<div class="abs center" style="top:2765px;color:#fff;font-size:14px">TESTIMONIALS</div>
<div class="abs center section-title" style="top:2783px;color:#fff">WHAT OUR CUSTOMERS SAY</div>
<div class="rule" style="top:2830px;left:558px;width:84px"></div>

<div class="round-arrow" style="top:3009px;left:93px;background:#ddd"><svg width="14" height="14" viewBox="0 0 14 14"><path d="M12 7H2M6 3L2 7l4 4" stroke="#555" stroke-width="2" fill="none"/></svg></div>
<div class="t-card" style="left:141px"><div class="avatar" role="img" aria-label="Client portrait"></div><h4>Ronan Pell</h4><p>Lorem ipsum dolor sit amet, consectetur adipiscing elit, sed do eiusmod tempor incididunt ut labore et dolore magna aliqua. Ut enim ad minim veniam.</p><div class="stars">★★★★★</div></div>
<div class="t-card" style="left:455px"><div class="avatar" role="img" aria-label="Client portrait"></div><h4>Hollis Whitmarsh</h4><p>Lorem ipsum dolor sit amet, consectetur adipiscing elit, sed do eiusmod tempor incididunt ut labore et dolore magna aliqua. Ut enim ad minim veniam.</p><div class="stars">★★★★★</div></div>
<div class="t-card" style="left:769px"><div class="avatar" role="img" aria-label="Client portrait"></div><h4>Peyton Walsh</h4><p>Lorem ipsum dolor sit amet, consectetur adipiscing elit, sed do eiusmod tempor incididunt ut labore et dolore magna aliqua. Ut enim ad minim veniam.</p><div class="stars">★★★★★</div></div>
<div class="round-arrow" style="top:3009px;left:1071px;background:var(--rose)"><svg width="14" height="14" viewBox="0 0 14 14"><path d="M2 7h10M8 3l4 4-4 4" stroke="#fff" stroke-width="2" fill="none"/></svg></div>

<section class="abs cta">
  <p>Empower Your Decisions With Expert<br>Policy Insights – Reach Out Now!</p>
  <div class="btn">Contact Us</div>
</section>

<footer class="abs footer">
  <div class="abs brand" style="top:56px;left:141px">
    <div class="brand-mark"></div>
    <div class="brand-name" style="color:#fff">FERNWAY<small>STRATEGY GROUP</small></div>
  </div>
  <div class="abs" style="top:54px;left:446px">
    <h5>Quick Links</h5>
    <ul><li>Home</li><li>Services</li><li>Research</li><li>The Institute</li><li>In The News</li><li>Contact Us</li></ul>
  </div>
  <div class="abs" style="top:54px;left:628px;width:290px">
    <h5>Contact Details</h5>
    <div class="f-line" style="margin-top:16px"><svg width="16" height="18" viewBox="0 0 16 18"><path d="M8 17s6-6 6-10A6 6 0 0 0 2 7c0 4 6 10 6 10z" fill="none" stroke="#fff" stroke-width="1.5"/><circle cx="8" cy="7" r="2" fill="#fff"/></svg><span>418 Larkspur Ave, Suite 210, Fairhaven,<br>VA 22019</span></div>
    <div class="f-line" style="margin-top:20px"><svg width="16" height="14" viewBox="0 0 16 14"><rect x="1" y="2" width="14" height="10" fill="none" stroke="#fff" stroke-width="1.5"/><path d="M1 2l7 6 7-6" fill="none" stroke="#fff" stroke-width="1.5"/></svg><span>info@fernwaystrategygroup.com</span></div>
    <div class="f-line" style="margin-top:24px"><svg width="16" height="16" viewBox="0 0 16 16"><path d="M3 1l3 3-2 2c1 2 3 4 5 5l2-2 3 3-2 3C7 15 1 9 1 3z" fill="none" stroke="#fff" stroke-width="1.5"/></svg><span>555-014-2276</span></div>
  </div>
  <div class="abs" style="top:54px;left:987px">
    <h5>Follow Us</h5>
    <div class="f-line" style="margin-top:16px;align-items:center"><span style="width:12px;height:12px;border-radius:50%;border:1.5px solid #fff;display:inline-block"></span><span>Updates</span></div>
  </div>
  <div class="abs footer-rule"></div>
  <div class="abs copy">©2024 Fernway Strategy Group. All Rights Reserved.</div>
</footer>

</body>
</html>
```